Business Card Design

New business card design

Target Market(s)

Residential & Commercial Property Managers

Industry/Entity Type

Plumbing Services

Contact Information for Business Card

Name - Owen Tredgold, title - Director, Phone Number - 0431 862 507, email - owen@rvb-plumbing.com.au, Company ABN - 73 215 904 386,

Font styles to use
Sans Serif

Colors
0054AA
0677BA
7BADD7
CADEEF
E8F1F8

```html
<!DOCTYPE html>
<html lang="en">
<head>
<meta charset="UTF-8">
<title>RVB Plumbing Services – Business Card</title>
<link rel="stylesheet" href="https://fonts.googleapis.com/css2?family=Poppins:wght@300;400;600&display=swap">
<style>
  :root {
    --stage: #e4e5e8;
    --card-front: #6f6357;
    --card-back: #ffffff;
    --ink: #1b2430;
    --ink-soft: #3a3f46;
    --brand-blue: #0677ba;
    --accent-blue: #29a3df;
    --pale-blue: #e8f1f8;
    --rule: #8a8d92;
  }
  * { box-sizing: border-box; margin: 0; padding: 0; }
  html, body { width: 1200px; height: 800px; overflow: hidden; }
  body {
    background: var(--stage);
    font-family: "Poppins", sans-serif;
    display: flex;
    align-items: center;
    justify-content: center;
    gap: 60px;
  }
  .card {
    width: 525px;
    height: 300px;
    position: relative;
    overflow: hidden;
    box-shadow: 0 6px 18px rgba(0,0,0,0.12);
  }
  .card--front {
    background: var(--card-front);
    display: flex;
    align-items: center;
    justify-content: center;
  }
  .wordmark {
    display: flex;
    flex-direction: column;
    align-items: center;
    color: var(--ink);
    font-weight: 400;
  }
  .wordmark__name {
    font-size: 64px;
    line-height: 1;
    letter-spacing: 2px;
  }
  .wordmark__tag {
    font-size: 11px;
    letter-spacing: 7px;
    margin-top: 10px;
  }
  .card--back { background: var(--card-back); }
  .card--back .wordmark {
    position: absolute;
    top: 30px;
    left: 150px;
  }
  .card--back .wordmark__name { font-size: 56px; }
  .card--back .wordmark__tag { font-size: 10px; }
  .backdrop-circle {
    position: absolute;
    right: -40px;
    bottom: -60px;
    width: 260px;
    height: 260px;
    border-radius: 50%;
    background: var(--pale-blue);
  }
  .contact {
    position: absolute;
    left: 32px;
    top: 150px;
    right: 32px;
  }
  .contact__name {
    color: var(--accent-blue);
    font-weight: 600;
    font-size: 17px;
    line-height: 1.1;
  }
  .contact__title-row {
    display: flex;
    align-items: flex-end;
    gap: 2px;
  }
  .contact__title {
    color: var(--ink-soft);
    font-size: 14px;
    line-height: 1.2;
  }
  .contact__rule {
    flex: 1;
    height: 1px;
    background: var(--rule);
    margin-bottom: 3px;
  }
  .contact__line {
    display: flex;
    align-items: center;
    gap: 8px;
    font-size: 14px;
    color: var(--ink-soft);
    margin-top: 6px;
  }
  .contact__line svg { width: 13px; height: 13px; flex: none; }
  .abn {
    position: absolute;
    right: 30px;
    bottom: 22px;
    color: var(--accent-blue);
    font-size: 14px;
    position: absolute;
  }
</style>
</head>
<body>
  <section class="card card--front" aria-label="Business card front">
    <div class="wordmark">
      <span class="wordmark__name">rvb</span>
      <span class="wordmark__tag">plumbing services</span>
    </div>
  </section>

  <section class="card card--back" aria-label="Business card back">
    <div class="backdrop-circle"></div>
    <div class="wordmark">
      <span class="wordmark__name">rvb</span>
      <span class="wordmark__tag">plumbing services</span>
    </div>
    <div class="contact">
      <p class="contact__name">Owen Tredgold</p>
      <div class="contact__title-row">
        <span class="contact__title">Director</span>
        <span class="contact__rule"></span>
      </div>
      <p class="contact__line">
        <svg viewBox="0 0 24 24" aria-hidden="true"><path fill="var(--accent-blue)" d="M6.6 10.8a15 15 0 0 0 6.6 6.6l2.2-2.2a1 1 0 0 1 1-.25 11.4 11.4 0 0 0 3.6.57 1 1 0 0 1 1 1V20a1 1 0 0 1-1 1A17 17 0 0 1 3 4a1 1 0 0 1 1-1h3.5a1 1 0 0 1 1 1c0 1.25.2 2.45.57 3.57a1 1 0 0 1-.25 1z"/></svg>
        0431 862 507
      </p>
      <p class="contact__line">
        <svg viewBox="0 0 24 24" aria-hidden="true"><path fill="var(--accent-blue)" d="M2 5h20v14H2z M3 6l9 7 9-7" stroke="#fff" stroke-width="1.5"/></svg>
        owen@rvb-plumbing.com.au
      </p>
    </div>
    <p class="abn">ABN - 73 215 904 386</p>
  </section>
</body>
</html>
```